Brivond Technologies business card design

We need a business card designed with our new logo. it would be great if the card could communicate it is a technology based company.

Target Market(s)

system integrators

Industry/Entity Type

technology, IOT

Contact Information for Business Card

Name, designation, Address, telephone number, email address

Requirements
Must have
• logo and company name
Nice to have
• something to do with technology

```html
<!DOCTYPE html>
<html lang="en">
<head>
<meta charset="utf-8">
<title>Brivond Technologies – Business Card</title>
<link href="https://fonts.googleapis.com/css2?family=Exo+2:wght@400;500;700&display=swap" rel="stylesheet">
<style>
  :root {
    --stage-dark: #262626;
    --stage-light: #4a4a4a;
    --card: #222222;
    --card-edge: #f28c1a;
    --accent: #f7931e;
    --ink: #ffffff;
    --ink-soft: #d6d6d6;
    --trace: #3a3a3a;
  }
  * { margin: 0; padding: 0; box-sizing: border-box; }
  html, body { width: 1200px; height: 740px; overflow: hidden; }
  body {
    background: linear-gradient(135deg, var(--stage-dark) 0%, var(--stage-light) 100%);
    font-family: "Exo 2", sans-serif;
    position: relative;
  }
  .card {
    position: absolute;
    top: 215px;
    width: 540px;
    height: 310px;
    background: var(--card);
    border-radius: 24px;
    border: 2px solid var(--card-edge);
    overflow: hidden;
    box-shadow: 0 18px 40px rgba(0,0,0,0.45);
  }
  .card--front { left: 45px; }
  .card--back { left: 615px; }

  .front-lines { position: absolute; inset: 0; }

  .holder { position: absolute; right: 282px; top: 118px; text-align: right; }
  .holder__name {
    color: var(--ink); font-weight: 700; font-size: 27px; letter-spacing: 1.5px; line-height: 1;
  }
  .holder__role {
    color: var(--accent); font-weight: 500; font-size: 16px; letter-spacing: 0.8px; margin-top: 6px;
  }

  .contact { position: absolute; left: 300px; top: 112px; list-style: none; }
  .contact__item {
    display: flex; align-items: center; gap: 9px;
    color: var(--ink-soft); font-size: 14px; letter-spacing: 0.4px; height: 24px;
  }
  .contact__icon { width: 12px; height: 12px; flex: none; }

  .front-brand {
    position: absolute; right: 38px; bottom: 36px;
    display: flex; align-items: center; gap: 8px;
  }
  .brand-square { background: var(--accent); flex: none; }
  .front-brand .brand-square { width: 12px; height: 12px; }
  .brand-name { color: var(--ink); font-weight: 700; letter-spacing: 1px; text-transform: uppercase; }
  .front-brand .brand-name { font-size: 13px; }

  .trace-field { position: absolute; left: 0; right: 0; }
  .trace-field--top { top: 0; height: 95px;
    background: linear-gradient(180deg, var(--trace) 0%, rgba(58,58,58,0) 100%); }
  .trace-field--bottom { bottom: 0; height: 95px;
    background: linear-gradient(0deg, var(--trace) 0%, rgba(58,58,58,0) 100%); }

  .back-brand {
    position: absolute; left: 0; right: 0; top: 50%; transform: translateY(-50%);
    display: flex; align-items: center; justify-content: center; gap: 18px;
  }
  .back-brand .brand-square { width: 58px; height: 58px; }
  .back-brand__words { display: flex; flex-direction: column; line-height: 1; }
  .back-brand .brand-name--main { font-size: 48px; letter-spacing: 2px; }
  .back-brand .brand-name--sub { font-size: 17px; letter-spacing: 7px; margin-top: 8px; }
</style>
</head>
<body>

<section class="card card--front" aria-label="Card front">
  <svg class="front-lines" width="540" height="310" viewBox="0 0 540 310">
    <g stroke="#f7931e" stroke-width="1.6" fill="#f7931e">
      <line x1="118" y1="203" x2="273" y2="203"/>
      <line x1="273" y1="203" x2="273" y2="88"/>
      <circle cx="118" cy="203" r="2.8"/>
      <circle cx="273" cy="88" r="2.8"/>
    </g>
    <g stroke="#ffffff" stroke-width="1.4" fill="#ffffff">
      <line x1="286" y1="96" x2="286" y2="196"/>
      <line x1="286" y1="96" x2="500" y2="96"/>
      <circle cx="500" cy="96" r="2.6"/>
      <circle cx="286" cy="196" r="2.6"/>
    </g>
  </svg>

  <div class="holder">
    <div class="holder__name">DANIEL HART</div>
    <div class="holder__role">Founder &amp; CEO</div>
  </div>

  <ul class="contact">
    <li class="contact__item">
      <svg class="contact__icon" viewBox="0 0 12 12"><path fill="#f7931e" d="M2.5 0.8l2 2.2-1 1.3c0.6 1.5 1.7 2.6 3.2 3.2l1.3-1 2.2 2-1.2 2.1C4.8 10.4 1.6 7.2 0.4 3.1z"/></svg>
      (555) 018-2047
    </li>
    <li class="contact__item">
      <svg class="contact__icon" viewBox="0 0 12 12"><rect x="0.5" y="2" width="11" height="8" fill="#f7931e"/><path d="M0.5 2.3L6 6.6l5.5-4.3" stroke="#222" stroke-width="1.2" fill="none"/></svg>
      dh@brivondtechnologies.com
    </li>
    <li class="contact__item">
      <svg class="contact__icon" viewBox="0 0 12 12"><circle cx="6" cy="6" r="5.2" fill="#f7931e"/><path d="M0.8 6h10.4M6 0.8c-2 2.8-2 7.6 0 10.4M6 0.8c2 2.8 2 7.6 0 10.4" stroke="#222" stroke-width="0.9" fill="none"/></svg>
      brivondtechnologies.com
    </li>
  </ul>

  <div class="front-brand">
    <span class="brand-square"></span>
    <span class="brand-name">Brivond Technologies</span>
  </div>
</section>

<section class="card card--back" aria-label="Card back">
  <div class="trace-field trace-field--top" role="img" aria-label="Circuit trace lines with node dots running down from the top edge"></div>
  <div class="trace-field trace-field--bottom" role="img" aria-label="Circuit trace lines with node dots rising from the bottom edge"></div>

  <div class="back-brand">
    <span class="brand-square"></span>
    <div class="back-brand__words">
      <span class="brand-name brand-name--main">Brivond</span>
      <span class="brand-name brand-name--sub">Technologies</span>
    </div>
  </div>
</section>

</body>
</html>
```